Home Water Filter Product Labels

We are looking for label design for a home water filter system. Attached files include examples of similar systems with sample labels. The file attached as Brightrill logo is our brand/logo and should be incorporated into each label and the text file explains what text should be included on each label of the system. There are a total of 6 labels on the system, 3 of which should be identical except for text and color.
Design Requirements:
-The attached logo should be used on the labels.
-The colors in the label should be used throughout the labels
-Label 1,2,3 should be the same design but different colors like the examples
-Labels Should not be copies of the examples but similar layout with different design
-Design needs to represent a clean feeling but can also be slightly industrial
-The finished files need to have the text editable in case we need to change wording.

Industry/Entity Type

Product

Font styles to use
Sans Serif

Colors

Designer to choose colors to be used in the design.

Requirements
Must have
• ***ALL DESIGN DIMENSIONS ARE IN INCHES**
• Labels 1-3:
• - Same design different colors for each label
• label 6:
• - Must incorporate our logo but include "Crest Range"

```html
<!DOCTYPE html>
<html lang="en">
<head>
<meta charset="UTF-8">
<title>Brightrill Sediment Filter Label</title>
<link href="https://fonts.googleapis.com/css2?family=Oswald:wght@500;700&family=Roboto:wght@400;500&display=swap" rel="stylesheet">
<style>
  :root {
    --navy: #0d2a4a;
    --blue: #1e9ad8;
    --green: #5aa832;
    --teal-green: #21a37a;
    --ink: #1d1d1f;
    --paper-top: #ffffff;
    --paper-bottom: #e9ebee;
  }
  * { margin: 0; padding: 0; box-sizing: border-box; }
  html, body { width: 843px; height: 1200px; overflow: hidden; background: #fff; }
  .label {
    position: relative;
    width: 843px;
    height: 1200px;
    overflow: hidden;
    background: linear-gradient(180deg, var(--paper-top) 0%, var(--paper-bottom) 100%);
    font-family: "Roboto", Arial, sans-serif;
    color: var(--ink);
  }
  .brand {
    position: absolute;
    top: 42px; left: 0; width: 100%;
    display: flex; justify-content: center; align-items: center; gap: 22px;
  }
  .brand-dot { width: 62px; height: 62px; border-radius: 50%; background: var(--blue); }
  .brand-name {
    font-family: "Oswald", sans-serif; font-weight: 700;
    font-size: 96px; line-height: 1; color: var(--blue); text-transform: uppercase;
  }
  .product {
    position: absolute; top: 168px; left: 0; width: 100%; text-align: center;
    font-family: "Oswald", sans-serif; font-weight: 700; text-transform: uppercase; line-height: 1.05;
  }
  .product-name { font-size: 70px; color: var(--teal-green); letter-spacing: 1px; }
  .product-range { font-size: 50px; color: var(--blue); letter-spacing: 1px; }
  .requirements { position: absolute; top: 312px; left: 46px; right: 40px; }
  .requirements h2 {
    font-family: "Oswald", sans-serif; font-weight: 700; font-size: 56px;
    text-transform: uppercase; text-align: center; line-height: 1.1; margin-bottom: 22px;
  }
  .spec { font-family: "Oswald", sans-serif; font-weight: 500; font-size: 37px; line-height: 1.25; text-transform: uppercase; }
  .spec strong { font-weight: 700; }
  .service-note { font-size: 25px; line-height: 1.4; margin-top: 18px; color: #333; }
  .warning { position: absolute; top: 640px; left: 46px; width: 560px; }
  .warning h3 {
    font-family: "Oswald", sans-serif; font-weight: 500; font-size: 38px;
    color: var(--blue); text-transform: uppercase; margin-bottom: 6px;
  }
  .warning p { font-size: 25px; line-height: 1.4; color: #333; }
  .artwork { position: absolute; left: 0; top: 0; }
  .web {
    position: absolute; bottom: 14px; left: 0; width: 100%; text-align: center;
    font-size: 22px; color: #fff; letter-spacing: 0.5px;
  }
</style>
</head>
<body>
<div class="label">
  <svg class="artwork" width="843" height="1200" viewBox="0 0 843 1200">
    <defs>
      <linearGradient id="towers" x1="0" y1="0" x2="0" y2="1">
        <stop offset="0" stop-color="#8fb8d8"/><stop offset="0.5" stop-color="#5a7f9f"/><stop offset="1" stop-color="#2d4358"/>
      </linearGradient>
      <linearGradient id="refinery" x1="0" y1="0" x2="0" y2="1">
        <stop offset="0" stop-color="#1c2f5a"/><stop offset="0.7" stop-color="#34507e"/><stop offset="1" stop-color="#d7a44a"/>
      </linearGradient>
      <linearGradient id="plant" x1="0" y1="0" x2="0" y2="1">
        <stop offset="0" stop-color="#1a1d2a"/><stop offset="0.6" stop-color="#6a4a3a"/><stop offset="1" stop-color="#0f121a"/>
      </linearGradient>
    </defs>
    <!-- curved bands -->
    <path d="M843 760 C 700 900 420 980 0 1000 L0 1200 L843 1200 Z" fill="var(--blue)"/>
    <path d="M843 820 C 700 960 430 1030 0 1050 L0 1200 L843 1200 Z" fill="var(--green)"/>
    <path d="M843 880 C 710 1010 450 1080 0 1100 L0 1200 L843 1200 Z" fill="#ffffff"/>
    <path d="M843 960 C 720 1070 520 1130 0 1150 L0 1200 L843 1200 Z" fill="var(--navy)"/>
    <!-- image areas -->
    <circle cx="660" cy="900" r="128" fill="var(--green)"/>
    <circle cx="660" cy="900" r="112" fill="url(#refinery)" role="img" aria-label="Industrial refinery lit at night"/>
    <circle cx="750" cy="1100" r="142" fill="var(--green)"/>
    <circle cx="750" cy="1100" r="126" fill="url(#plant)" role="img" aria-label="Power plant cooling tower with steam at dusk"/>
    <circle cx="175" cy="1050" r="190" fill="var(--green)"/>
    <circle cx="175" cy="1050" r="172" fill="url(#towers)" role="img" aria-label="Twin skyscrapers viewed from below"/>
  </svg>

  <header class="brand">
    <span class="brand-dot"></span>
    <span class="brand-name">Brightrill</span>
  </header>

  <div class="product">
    <div class="product-name">Sediment Filter</div>
    <div class="product-range">Crest Range: 1 Micron</div>
  </div>

  <section class="requirements">
    <h2>Operating Requirements:</h2>
    <p class="spec"><strong>Temperature:</strong> Min 4°C 49°F, Max 52°C 125°F</p>
    <p class="spec"><strong>Pressure:</strong> Min 35PSI 241KPA, Max 80PSI 551KPA</p>
    <p class="service-note">Manufacturers recommendation is to replace every 6-9<br>Months depending on incomming water quality</p>
  </section>

  <section class="warning">
    <h3>Warning</h3>
    <p>When intended use is for drinking water make sure water is microbiologically safe or adequate disinfection is performed before or after system.</p>
  </section>

  <div class="web">www.brightrillfilters.com</div>
</div>
</body>
</html>
```